Tidy Haven Path half fold brochure design

I need a brochure for a new company. The name of the company is Tidy Haven Path. I am a Professional Organizer. I am requesting a one fold brochure 11" wide x 8.5" high (obviously once folded 5.5" wide x 8.5" high) brochure. I have been told this may need to be designed as a flyer? I have attached a VERY BASIC layout of what I think I am looking for. I have also attached the original logos in all the different formats I have. I would like to have a very light green background & the text I have in orange please make orange. PLEASE feel free to add color to my "Tidy Haven Path" logo's and use light/soft green & orange shades if possible (OK to go darker for BOLD purposes) The brochure DOES NOT have to stick to this layout, again just what I THINK I want :) - THANK YOU

EDIT: 01-21-15 Remove MARLENE KUDSIK from all 3 places (front, bottom inside right & back) Remove just the KUDSIK from the 1st line on the back. PRIVACY & ETHICS on the back, please remove "PRIVACY &", leave Ethics and the 1st line of the text under it. Please remove all of the text following the 1st sentence. THANK YOU

Industry/Entity Type

It Company

```html
<!DOCTYPE html>
<html lang="en">
<head>
<meta charset="utf-8">
<title>Tidy Haven Path – Inside Spread</title>
<link href="https://fonts.googleapis.com/css2?family=Quicksand:wght@400;500;600;700&display=swap" rel="stylesheet">
<style>
  :root {
    --backdrop: #e6e6e6;
    --green-strong: #8cc63f;
    --green-mid: #a9d46a;
    --green-pale: #dcedc0;
    --green-mist: #eef6e2;
    --orange: #e0571f;
    --chip-orange: #d98a2b;
    --ink: #2a2a2a;
    --ink-soft: #3d3d3d;
    --white: #ffffff;
    --photo-warm: #c9a882;
    --photo-cream: #efe3cf;
    --photo-wood: #9c7450;
  }
  * { box-sizing: border-box; margin: 0; padding: 0; }
  html, body { width: 1200px; height: 800px; overflow: hidden; }
  body {
    background: var(--backdrop);
    font-family: "Quicksand", sans-serif;
    color: var(--ink);
  }
  .spread {
    position: absolute;
    left: 108px; top: 20px;
    width: 984px; height: 760px;
    display: flex;
    box-shadow: 0 2px 10px rgba(0,0,0,.15);
  }
  .page {
    position: relative;
    width: 492px; height: 760px;
    overflow: hidden;
  }
  .page--left {
    background: linear-gradient(120deg, var(--green-mist) 0%, var(--green-pale) 35%, #f3f9ea 50%, var(--green-mid) 100%);
  }
  .page--right {
    background: linear-gradient(160deg, var(--green-pale) 0%, var(--green-mist) 40%, #cfe6a8 100%);
  }

  /* Left page */
  .hero-photo {
    position: absolute; left: 0; top: 0;
    width: 492px; height: 240px;
    background: linear-gradient(180deg, var(--photo-cream) 0%, var(--photo-warm) 60%, var(--photo-wood) 100%);
  }
  .hero-wave { position: absolute; left: 0; top: 170px; width: 492px; height: 90px; }
  .col {
    position: absolute;
    font-size: 11px; line-height: 1.5;
    color: var(--ink-soft);
  }
  .col--first { left: 30px; top: 268px; width: 212px; }
  .col--second { left: 258px; top: 236px; width: 210px; }
  .lead {
    font-size: 14px; line-height: 1.28; font-weight: 500;
    color: var(--ink); margin-bottom: 8px; padding-left: 4px;
  }
  .question {
    color: var(--orange);
    font-size: 13.5px; font-weight: 600; line-height: 1.25;
    margin: 6px 0 5px;
  }
  .col p { margin-bottom: 9px; }
  .col--first p:not(.lead) { padding-left: 6px; }
  .closing {
    font-size: 13px; font-weight: 700; line-height: 1.3;
    color: var(--ink); text-transform: uppercase; letter-spacing: .3px;
    margin-top: 4px;
  }

  /* Right page */
  .intro-band { position: absolute; left: 0; top: 0; width: 492px; height: 310px; }
  .intro {
    position: absolute; left: 30px; top: 26px; width: 440px;
    font-size: 11px; line-height: 1.5; color: var(--ink-soft);
  }
  .intro h2 {
    text-align: center; font-size: 15.5px; font-weight: 700;
    color: var(--ink); margin-bottom: 8px;
  }
  .intro p { margin-bottom: 10px; }
  .intro .attribution { font-weight: 700; display: block; }

  .services {
    position: absolute; left: 0; top: 318px; width: 492px;
    display: flex; flex-direction: column; align-items: center;
    text-align: center;
  }
  .service-title {
    font-size: 15px; font-weight: 700; letter-spacing: .4px;
    color: var(--ink); margin: 12px 0 5px;
  }
  .service-title:first-child { margin-top: 0; }
  .service-note { font-size: 12.5px; font-weight: 600; margin-top: 5px; }
  .steps { display: flex; }
  .step {
    height: 26px; min-width: 96px; padding: 0 18px 0 22px;
    display: flex; align-items: center; justify-content: center;
    font-size: 12.5px; font-weight: 600; color: var(--ink);
    background: var(--white);
    clip-path: polygon(0 0, calc(100% - 13px) 0, 100% 50%, calc(100% - 13px) 100%, 0 100%, 13px 50%);
    margin-left: -9px;
  }
  .step:first-child { clip-path: polygon(0 0, calc(100% - 13px) 0, 100% 50%, calc(100% - 13px) 100%, 0 100%); margin-left: 0; padding-left: 14px; }
  .step--accent { background: var(--chip-orange); }
  .removal-list { list-style: none; font-size: 12.5px; font-weight: 600; line-height: 1.35; }
  .removal-list li::before { content: "• "; }
  .contact-line { font-size: 13px; font-weight: 500; margin-top: 14px; color: var(--ink-soft); }
</style>
</head>
<body>
  <main class="spread">
    <section class="page page--left">
      <div class="hero-photo" role="img" aria-label="Photo of a tidy living room with wood stove, television, bookshelves and sofa"></div>
      <svg class="hero-wave" viewBox="0 0 492 90" preserveAspectRatio="none" aria-hidden="true">
        <path d="M0 55 C 150 92, 330 55, 492 8 L492 90 L0 90 Z" fill="var(--white)"/>
        <path d="M0 64 C 150 100, 330 64, 492 20 L492 90 L0 90 Z" fill="var(--green-mist)"/>
      </svg>

      <div class="col col--first">
        <p class="lead">Getting organized isn’t all about everything being in its proper place.</p>
        <p class="lead">It can also require overcoming fears and anxieties such as:</p>
        <h3 class="question">How do I start?</h3>
        <p>You begin by getting help from a professional. No one can do everything; everyone needs a helping hand at times. (I bring my vehicle to a mechanic when it needs service, even for just a simple oil change!)</p>
        <h3 class="question">Am I going to have to get rid of ALL my things?</h3>
        <p>Definitely not! There is a process that will help you decide what to keep and what you would be willing to part with. (I can help you determine the practical and monetary “worth” of something. Only you can determine its personal “value”.)</p>
      </div>

      <div class="col col--second">
        <h3 class="question">I don’t have time</h3>
        <p>Now you will! Getting organized will actually save you time. You will know where that “thing” is, find it quickly and avoid the time it takes to run out and purchase a new “thing”. (You will have actually created more time to enjoy the lifestyle that is important to you.)</p>
        <p>We all have anxiety about something that prevents or inhibits us from taking action toward a solution. Whether you want someone to take over the project or a helping hand (nudge) is all you really need, a professional organizer is the perfect way to get started. Getting organized is going to be a process of progress, not perfection. It will require some level of support and continued work on you part, but the rewards will far outweigh the efforts.</p>
        <p class="closing">Together we can conquer the clutter and create clarity</p>
      </div>
    </section>

    <section class="page page--right">
      <svg class="intro-band" viewBox="0 0 492 310" preserveAspectRatio="none" aria-hidden="true">
        <path d="M0 0 H492 V255 C 380 285, 260 235, 150 268 C 90 288, 40 292, 0 284 Z" fill="var(--green-strong)"/>
      </svg>
      <div class="intro">
        <h2>What is a professional organizer?</h2>
        <p>A Professional Organizer enhances the lives of clients by designing systems and processes using organizing principles and through transferring organizing skills. Professional Organizers help individuals and businesses take control of their surroundings, their time, their paper, and their systems for life.”
          <span class="attribution">– Guild of Home Organizing Specialists</span></p>
        <p>Whether you are too busy, too confused, over whelmed, tired, stressed or just don’t know where to start, I offer a variety of hands on services to help you bring a sense of fun, freedom and functionality to almost any space.</p>
      </div>

      <div class="services">
        <h3 class="service-title">ATTIC – TO – BASEMENT</h3>
        <div class="steps">
          <span class="step">Sorting</span><span class="step step--accent">Purging</span><span class="step">Organizing</span>
        </div>

        <h3 class="service-title">PAPER CONTROL</h3>
        <div class="steps">
          <span class="step">Sorting</span><span class="step step--accent">Purging</span><span class="step">Organizing</span>
        </div>
        <p class="service-note">Household, home office &amp; home based filing systems</p>

        <h3 class="service-title">DOWNSIZING</h3>
        <div class="steps">
          <span class="step">Sorting</span><span class="step step--accent">Purging</span><span class="step">Organizing</span><span class="step step--accent">Labeling</span>
        </div>
        <p class="service-note">Packing &amp; unpacking</p>

        <h3 class="service-title">REMOVAL</h3>
        <ul class="removal-list">
          <li>Light trash &amp; proper disposal</li>
          <li>Donations &amp; light recyclables to proper locations</li>
          <li>Shredding Service</li>
        </ul>

        <h3 class="service-title">FOLLOW UP</h3>
        <p class="service-note">Routine “clutter maintenance” visits</p>

        <p class="contact-line">For projects not listed above, please contact me.</p>
      </div>
    </section>
  </main>
</body>
</html>
```